Online interactive calendar for training organisation

We have a new website being made and need a design for an online calendar that is interactive and very simple and easy to use. On our main page this calendar will include all of our courses (approx 30 different ones with up to 8 different locations). On our sub pages which have course information, the calendar will only include details of that specific course. Details needed are: Course code, course name/title, date, duration (1/2 day - 5 days), location, price, discount price. Maybe also a key for available or limited spots left? We want a section at the top of the calendar to be able to filter by location or course, and maybe to filter by month also? I have included a spreadsheet with a sample of our courses with this information. Also a sample draft of the main page on our new webpage to show the colour green which is our company colour. Main notes - we want as simple, effective and easy to use as possible.
We will need to know what plug in we can use to get the design you have created.

Target Market(s)

Mining and construction - both companies and individuals

Number of Pages Required

1 page

Colors
cadf82

Requirements
Must have
• Be simple, easy to use, effective.

```html
<!DOCTYPE html>
<html lang="en">
<head>
<meta charset="utf-8">
<title>Keystone Safety – Time Table</title>
<link href="https://fonts.googleapis.com/css2?family=Dosis:wght@500&family=Montserrat:wght@400;500;700;800&family=Merriweather+Sans:ital,wght@0,300;0,400;1,300&display=swap" rel="stylesheet">
<style>
:root{
  --green:#95c83d;
  --green-soft:#b6d66c;
  --brand-red:#d6151b;
  --ink:#1e1e1e;
  --text:#555;
  --muted:#777;
  --grey-bg:#f1f1f1;
  --line:#bdbdbd;
  --footer:#2a2a2a;
  --white:#fff;
}
*{box-sizing:border-box;margin:0;padding:0}
html,body{width:1200px;height:2163px;overflow:hidden}
body{position:relative;background:var(--white);font-family:"Merriweather Sans",sans-serif;color:var(--text)}
.abs{position:absolute}

/* top bar */
.topbar{left:0;top:0;width:1200px;height:31px;background:var(--green)}
.social{left:226px;top:7px;display:flex;gap:5px}
.social span{width:18px;height:18px;border-radius:50%;background:#1b1b1b;display:block}
.student-btn{left:781px;top:5px;width:83px;height:21px;background:#1b1b1b;color:#fff;font:700 9px "Montserrat",sans-serif;display:flex;align-items:center;justify-content:center;border-radius:2px}
.search{left:870px;top:5px;width:108px;height:21px;background:#fff;border-radius:2px}
.search svg{position:absolute;right:8px;top:5px}

/* header */
.header{left:0;top:31px;width:1200px;height:70px;background:var(--white)}
.brand{left:228px;top:47px;display:flex;align-items:center;gap:8px}
.brand-mark{width:34px;height:34px;border-radius:50%;background:var(--brand-red)}
.brand-name{font:800 19px "Montserrat",sans-serif;color:var(--brand-red);letter-spacing:.5px;line-height:1}
.brand-sub{left:305px;top:77px;font:500 9px "Montserrat",sans-serif;color:#222;letter-spacing:.5px}
.nav{right:222px;top:60px;display:flex;gap:18px;font:400 9px "Montserrat",sans-serif;color:#333}
.nav .active{color:var(--green)}

/* difference */
.difference{left:0;top:101px;width:1200px;height:537px;background:var(--grey-bg)}
.diff-title{left:0;top:145px;width:1200px;text-align:center;font:500 30px "Dosis",sans-serif;color:#1e1e1e;letter-spacing:.3px}
.diff-sub{left:0;top:185px;width:1200px;text-align:center;font:400 11px "Merriweather Sans",sans-serif;color:#333}
.rule{height:3px;width:50px;background:var(--green-soft)}
.tile{width:139px;height:136px;border-radius:2px}
.tile-label{width:139px;text-align:center;font:400 11.5px "Merriweather Sans",sans-serif;color:#333}

/* timetable */
.tt-title{left:0;top:694px;width:1200px;text-align:center;font:400 32px "Montserrat",sans-serif;color:#111}
.login{right:145px;top:764px;font:300 15px "Merriweather Sans",sans-serif;color:var(--muted)}
.filter{top:795px;height:50px;border:1px solid var(--line);border-radius:25px;display:flex;align-items:center;justify-content:space-between;padding:0 20px;font:300 15px "Merriweather Sans",sans-serif;color:#555;background:#fff}
.card{width:286px;height:260px;background:#fff;box-shadow:0 1px 8px rgba(0,0,0,.13);border-radius:3px;padding:19px 0 0 27px}
.card-title{font:500 19px "Montserrat",sans-serif;color:#111;line-height:24px;width:250px;height:56px}
.card-title .star{color:var(--brand-red)}
.row{display:flex;gap:20px;font:300 14.5px "Merriweather Sans",sans-serif;color:#555;line-height:23px}
.row svg{flex:none;margin-top:5px}
.row .icon{width:16px;display:flex;justify-content:center}
.r-date{margin-top:0}
.r-time{margin-top:13px}
.r-loc{margin-top:13px}
.r-price{margin-top:10px}
.dollar{color:var(--green-soft);font-weight:400;font-size:17px}
.old{color:var(--green-soft);text-decoration:line-through;width:68px;font-size:13px}
.dash{color:var(--green-soft);width:68px}
.limited{left:140px;top:1463px;font:italic 300 14px "Merriweather Sans",sans-serif;color:var(--brand-red)}

/* banner */
.banner{left:0;top:1538px;width:1200px;height:407px}
.banner-frame{left:764px;top:1603px;width:243px;height:278px;border:10px solid #fff;box-shadow:3px 3px 0 rgba(0,0,0,.12)}
.banner-title{left:651px;top:1689px;font:800 40px "Montserrat",sans-serif;color:#1d1d1d;line-height:43px;letter-spacing:-.3px}
.banner-strip{left:651px;top:1787px;width:328px;height:24px;background:var(--green);color:#fff;font:500 9.5px "Montserrat",sans-serif;display:flex;align-items:center;justify-content:center}

/* footer */
.footer{left:0;top:1945px;width:1200px;height:177px;background:var(--footer)}
.f-brand{left:224px;top:1996px;display:flex;align-items:center;gap:8px}
.f-brand .brand-mark{width:32px;height:32px}
.follow{left:268px;top:2048px;display:flex;align-items:center;gap:6px;font:400 11px "Merriweather Sans",sans-serif;color:#ddd}
.follow span{width:17px;height:17px;background:#111;display:block;border-radius:2px}
.f-nav{right:222px;top:2013px;display:flex;gap:18px;font:400 8.5px "Montserrat",sans-serif;color:#ddd}
.contact{top:2047px;display:flex;align-items:center;gap:10px;font:400 9.5px "Montserrat",sans-serif;color:#ddd}
.contact .ico{width:23px;height:23px;background:#111;display:flex;align-items:center;justify-content:center}
.to-top{left:1009px;top:2098px;width:36px;height:38px;background:#fff;display:flex;align-items:center;justify-content:center;border-radius:2px}
.bottombar{left:0;top:2122px;width:1200px;height:41px;background:var(--green);display:flex;align-items:center;justify-content:center;font:400 9px "Merriweather Sans",sans-serif;color:#333}
</style>
</head>
<body>

<!-- top bar -->
<div class="abs topbar"></div>
<div class="abs social"><span></span><span></span><span></span><span></span></div>
<div class="abs student-btn">Student Access</div>
<div class="abs search"><svg width="10" height="10" viewBox="0 0 10 10"><circle cx="4" cy="4" r="3" fill="none" stroke="#111" stroke-width="1.6"/><line x1="6.2" y1="6.2" x2="9" y2="9" stroke="#111" stroke-width="1.8"/></svg></div>

<!-- header -->
<div class="abs header"></div>
<div class="abs brand"><span class="brand-mark"></span><span class="brand-name">KEYSTONE SAFETY</span></div>
<div class="abs brand-sub">SAFETY AND TRAINING</div>
<nav class="abs nav"><span class="active">Home</span><span>Courses</span><span>Our Services</span><span>About us</span><span>Funding</span><span>Locations</span><span>Contact us</span></nav>

<!-- difference -->
<section class="abs difference"></section>
<h1 class="abs diff-title">THE KEYSTONE SAFETY DIFFERENCE</h1>
<p class="abs diff-sub">Committed to helping our students succeed.</p>
<div class="abs rule" style="left:575px;top:213px"></div>

<div class="abs tile" style="left:224px;top:245px;background:linear-gradient(160deg,#8a8780,#5f5c57)" role="img" aria-label="Photo of a wheel loader on a mining site"></div>
<div class="abs tile" style="left:376px;top:245px;background:linear-gradient(160deg,#74c3ee,#3d8fcf)" role="img" aria-label="Photo of a gloved handshake"></div>
<div class="abs tile" style="left:530px;top:245px;background:linear-gradient(160deg,#8f8d88,#a83a36)" role="img" aria-label="Photo of a red mining truck"></div>
<div class="abs tile" style="left:685px;top:245px;background:linear-gradient(160deg,#5a5652,#9a8345)" role="img" aria-label="Photo of an excavator in a quarry"></div>
<div class="abs tile" style="left:840px;top:245px;background:linear-gradient(160deg,#b9c1c8,#4e5358)" role="img" aria-label="Photo of workers at heights on a roof"></div>
<div class="abs tile-label" style="left:224px;top:395px">All Courses</div>
<div class="abs tile-label" style="left:376px;top:395px">Funded courses</div>
<div class="abs tile-label" style="left:530px;top:395px">Mining</div>
<div class="abs tile-label" style="left:685px;top:395px">Standard 11</div>
<div class="abs tile-label" style="left:840px;top:395px">Work safely at heights</div>

<div class="abs tile" style="left:224px;top:428px;background:linear-gradient(160deg,#6d7479,#2f3338)" role="img" aria-label="Photo of corporate clients at a meeting"></div>
<div class="abs tile" style="left:376px;top:428px;background:linear-gradient(160deg,#c7c2bb,#d49a3a)" role="img" aria-label="Photo of students around a laptop"></div>
<div class="abs tile" style="left:530px;top:428px;background:linear-gradient(160deg,#7ab6e0,#c9d84a)" role="img" aria-label="Photo of site workers reviewing plans"></div>
<div class="abs tile" style="left:685px;top:428px;background:linear-gradient(160deg,#8b9096,#d6c23a)" role="img" aria-label="Photo of an operator with an elevated work platform"></div>
<div class="abs tile" style="left:840px;top:428px;background:linear-gradient(160deg,#b07a48,#4a4440)" role="img" aria-label="Photo of a construction worker on formwork"></div>
<div class="abs tile-label" style="left:224px;top:578px">Corporate clients</div>
<div class="abs tile-label" style="left:376px;top:578px">Online courses</div>
<div class="abs tile-label" style="left:530px;top:578px">RPL's &amp; VOC's</div>
<div class="abs tile-label" style="left:685px;top:578px">Plant &amp; Equipment</div>
<div class="abs tile-label" style="left:840px;top:578px">Construction</div>

<!-- timetable -->
<h2 class="abs tt-title">Time Table</h2>
<div class="abs rule" style="left:575px;top:741px"></div>
<div class="abs login">Login / Register</div>

<div class="abs filter" style="left:137px;width:281px">Location<svg width="10" height="6" viewBox="0 0 10 6"><path d="M1 1l4 4 4-4" fill="none" stroke="#444" stroke-width="1.4"/></svg></div>
<div class="abs filter" style="left:437px;width:327px">Course<svg width="10" height="6" viewBox="0 0 10 6"><path d="M1 1l4 4 4-4" fill="none" stroke="#444" stroke-width="1.4"/></svg></div>
<div class="abs filter" style="left:782px;width:282px">Month<svg width="10" height="6" viewBox="0 0 10 6"><path d="M1 1l4 4 4-4" fill="none" stroke="#444" stroke-width="1.4"/></svg></div>

<article class="abs card" style="left:140px;top:887px">
  <h3 class="card-title">RIIMPO308E Forklift<span class="star">*</span></h3>
  <div class="row r-date"><span class="icon"><svg width="15" height="14" viewBox="0 0 15 14"><rect x="1" y="2" width="13" height="11" fill="none" stroke="#b6d66c" stroke-width="1.4"/><rect x="1" y="2" width="13" height="3" fill="#b6d66c"/><path d="M4 7h2M7 7h2M10 7h2M4 10h2M7 10h2M10 10h2" stroke="#b6d66c"/></svg></span>Wednesday, October 30, 2019</div>
  <div class="row r-time"><span class="icon"><svg width="14" height="14" viewBox="0 0 14 14"><circle cx="7" cy="7" r="5.8" fill="none" stroke="#b6d66c" stroke-width="1.6"/><path d="M7 4v3.5h2.5" fill="none" stroke="#b6d66c" stroke-width="1.4"/></svg></span><span>3 days ;<br>8 am</span></div>
  <div class="row r-loc"><span class="icon"><svg width="11" height="15" viewBox="0 0 11 15"><path d="M5.5 14S1 8.6 1 5.5a4.5 4.5 0 0 1 9 0C10 8.6 5.5 14 5.5 14z" fill="#b6d66c"/><circle cx="5.5" cy="5.3" r="1.7" fill="#fff"/></svg></span>Mackay</div>
  <div class="row r-price"><span class="icon dollar">$</span><span class="old">$ 100.00</span><span>$ 500.00</span></div>
</article>

<article class="abs card" style="left:458px;top:887px">
  <h3 class="card-title">HLTAID001 First Aid - practical only</h3>
  <div class="row r-date"><span class="icon"><svg width="15" height="14" viewBox="0 0 15 14"><rect x="1" y="2" width="13" height="11" fill="none" stroke="#b6d66c" stroke-width="1.4"/><rect x="1" y="2" width="13" height="3" fill="#b6d66c"/><path d="M4 7h2M7 7h2M10 7h2M4 10h2M7 10h2M10 10h2" stroke="#b6d66c"/></svg></span>Saturday, November 30, 2019</div>
  <div class="row r-time"><span class="icon"><svg width="14" height="14" viewBox="0 0 14 14"><circle cx="7" cy="7" r="5.8" fill="none" stroke="#b6d66c" stroke-width="1.6"/><path d="M7 4v3.5h2.5" fill="none" stroke="#b6d66c" stroke-width="1.4"/></svg></span><span>1/2 day ;<br>8 am</span></div>
  <div class="row r-loc"><span class="icon"><svg width="11" height="15" viewBox="0 0 11 15"><path d="M5.5 14S1 8.6 1 5.5a4.5 4.5 0 0 1 9 0C10 8.6 5.5 14 5.5 14z" fill="#b6d66c"/><circle cx="5.5" cy="5.3" r="1.7" fill="#fff"/></svg></span>Mackay</div>
  <div class="row r-price"><span class="icon dollar">$</span><span class="dash">-</span><span>$ 80.00</span></div>
</article>

<article class="abs card" style="left:776px;top:887px">
  <h3 class="card-title">Defensive Driving</h3>
  <div class="row r-date"><span class="icon"><svg width="15" height="14" viewBox="0 0 15 14"><rect x="1" y="2" width="13" height="11" fill="none" stroke="#b6d66c" stroke-width="1.4"/><rect x="1" y="2" width="13" height="3" fill="#b6d66c"/><path d="M4 7h2M7 7h2M10 7h2M4 10h2M7 10h2M10 10h2" stroke="#b6d66c"/></svg></span>Wednesday, November 27, 2019</div>
  <div class="row r-time"><span class="icon"><svg width="14" height="14" viewBox="0 0 14 14"><circle cx="7" cy="7" r="5.8" fill="none" stroke="#b6d66c" stroke-width="1.6"/><path d="M7 4v3.5h2.5" fill="none" stroke="#b6d66c" stroke-width="1.4"/></svg></span><span>1 days ;<br>8 am</span></div>
  <div class="row r-loc"><span class="icon"><svg width="11" height="15" viewBox="0 0 11 15"><path d="M5.5 14S1 8.6 1 5.5a4.5 4.5 0 0 1 9 0C10 8.6 5.5 14 5.5 14z" fill="#b6d66c"/><circle cx="5.5" cy="5.3" r="1.7" fill="#fff"/></svg></span>Mackay</div>
  <div class="row r-price"><span class="icon dollar">$</span><span class="dash">-</span><span>$ 275.00</span></div>
</article>

<article class="abs card" style="left:138px;top:1187px">
  <h3 class="card-title">HLTAID001 First Aid - practical only</h3>
  <div class="row r-date"><span class="icon"><svg width="15" height="14" viewBox="0 0 15 14"><rect x="1" y="2" width="13" height="11" fill="none" stroke="#b6d66c" stroke-width="1.4"/><rect x="1" y="2" width="13" height="3" fill="#b6d66c"/><path d="M4 7h2M7 7h2M10 7h2M4 10h2M7 10h2M10 10h2" stroke="#b6d66c"/></svg></span>Wednesday, January 15, 2020</div>
  <div class="row r-time"><span class="icon"><svg width="14" height="14" viewBox="0 0 14 14"><circle cx="7" cy="7" r="5.8" fill="none" stroke="#b6d66c" stroke-width="1.6"/><path d="M7 4v3.5h2.5" fill="none" stroke="#b6d66c" stroke-width="1.4"/></svg></span><span>1/2 day;<br>1pm</span></div>
  <div class="row r-loc"><span class="icon"><svg width="11" height="15" viewBox="0 0 11 15"><path d="M5.5 14S1 8.6 1 5.5a4.5 4.5 0 0 1 9 0C10 8.6 5.5 14 5.5 14z" fill="#b6d66c"/><circle cx="5.5" cy="5.3" r="1.7" fill="#fff"/></svg></span>Mackay</div>
  <div class="row r-price"><span class="icon dollar">$</span><span class="dash">-</span><span>$ 80.00</span></div>
</article>

<p class="abs limited">limited spots left*</p>

<!-- banner -->
<div class="abs banner" role="img" aria-label="Photo of a large yellow mining haul truck on a dusty site" style="background:linear-gradient(90deg,#6f6a5e 0%,#a8923a 22%,#8b8677 40%,#cfcfcb 60%,#e3e3e0 80%,#d8d6cf 100%)"></div>
<div class="abs banner-frame"></div>
<h2 class="abs banner-title">Training a Safety<br>Culture that Counts</h2>
<div class="abs banner-strip">NOW TRAINING - Working at Heights &amp; Confined Spaces courses</div>

<!-- footer -->
<footer class="abs footer"></footer>
<div class="abs f-brand"><span class="brand-mark"></span><span class="brand-name">KEYSTONE SAFETY</span></div>
<div class="abs follow">Follow us on :-<span></span><span></span><span></span><span></span></div>
<nav class="abs f-nav"><span>Home</span><span>Courses</span><span>Our Services</span><span>About us</span><span>Funding</span><span>Locations</span><span>Contact us</span></nav>
<div class="abs contact" style="left:588px"><span class="ico"><svg width="9" height="12" viewBox="0 0 11 15"><path d="M5.5 14S1 8.6 1 5.5a4.5 4.5 0 0 1 9 0C10 8.6 5.5 14 5.5 14z" fill="#fff"/><circle cx="5.5" cy="5.3" r="1.7" fill="#111"/></svg></span>18 Depot Road, Ridgefield QLD 4300</div>
<div class="abs contact" style="left:828px"><span class="ico"><svg width="12" height="9" viewBox="0 0 12 9"><rect width="12" height="9" fill="#fff"/><path d="M0 0l6 5 6-5" fill="none" stroke="#111" stroke-width="1.2"/></svg></span>office@keystonesafety.example</div>
<div class="abs to-top"><svg width="14" height="8" viewBox="0 0 14 8"><path d="M1 7l6-6 6 6" fill="none" stroke="#222" stroke-width="1.8"/></svg></div>
<div class="abs bottombar">© Copyright All Right Reserved | Powered by Keystone Safety.</div>

</body>
</html>
```